Vinyl Banner for bike shop to hang outside a railway station and attract new customers)

We run a small indenendent bike shop on the main campus at Halvercombe Institute.

Just up the road from us is the Halvercombe train station where thousands of commuters enter and exit each day.

We have permssion to hang a vinyl banner 1.2m x 3.5m directly opposite the ttrain station entrance/exit.

Vinyl Banner adverts must:
Clearly display Pondel Wheels logo
Include directional arrows pointing left.
List our email, url and phone details
Promote the purchasing of new bikes through Ridepathplan
Promote Bike Hire
Promote repairs and servicing of all bikes.
Promote sales of accesories including and especially Vornastel D locks
Be friendly to a female target audience without excluding men.
Be in keeping with our logo font etc.
Be a significant impovemnet on our current banner
Include logo's of our major brands (Tavoli Bikes, Palmwick Bikes, Oskel Bikes, Vush Bikes, Lappet Bikes, Quill Bikes)

Include "10% OFF for all PCW Staff'

I've added some image files you may or may not wish to use. All of which are currently used somewhere on our website.

Target Market(s)

Commuters, Students,

Industry/Entity Type

Shop

Requirements
Must have
• Our logo and brand logo's
Nice to have
• We generally use Exo font
Should not have
• Clip art!!!!

```html
<!DOCTYPE html>
<html lang="en">
<head>
<meta charset="utf-8">
<title>Pondel Wheels – Station Banner</title>
<link href="https://fonts.googleapis.com/css2?family=Exo+2:wght@400;500;600;700&display=swap" rel="stylesheet">
<style>
  :root {
    --teal: #2bb3a8;
    --navy: #1f4e70;
    --black: #111111;
    --white: #ffffff;
    --photo-light: #e9dcc8;
    --photo-mid: #b99a78;
    --photo-dark: #5a4a45;
    --strip: rgba(255, 255, 255, 0.82);
    --ink: #1a1a1a;
  }
  * { margin: 0; padding: 0; box-sizing: border-box; }
  html, body { width: 1200px; height: 411px; overflow: hidden; background: var(--white); }
  body { font-family: "Exo 2", sans-serif; }

  .banner { position: relative; width: 1200px; height: 411px; overflow: hidden; }

  .info-panel {
    position: absolute; left: 0; top: 0; width: 520px; height: 411px;
    background: var(--teal); color: var(--white);
  }
  .staff-offer {
    position: absolute; left: 26px; top: 16px; width: 106px; height: 106px;
    border-radius: 50%; background: var(--navy);
    display: flex; align-items: center; justify-content: center; text-align: center;
    font-weight: 600; font-size: 17px; line-height: 1.15;
  }
  .services {
    position: absolute; right: 24px; top: 14px; text-align: right;
    font-weight: 600; font-size: 34px; line-height: 40px; letter-spacing: -0.3px;
    white-space: nowrap;
  }
  .direction {
    position: absolute; left: 0; top: 226px; width: 520px; height: 74px;
  }
  .direction svg { position: absolute; inset: 0; }
  .direction-text {
    position: absolute; left: 86px; top: 9px; width: 420px; text-align: center;
    font-size: 22px; line-height: 28px; font-weight: 400;
  }
  .phone {
    position: absolute; left: 0; width: 520px; top: 308px; text-align: center;
    font-weight: 600; font-size: 37px;
  }
  .web {
    position: absolute; left: 0; width: 520px; top: 368px; text-align: center;
    font-size: 14px; letter-spacing: 1.2px; white-space: nowrap;
  }

  .photo-area {
    position: absolute; left: 520px; top: 0; width: 680px; height: 411px;
    background: linear-gradient(120deg, var(--photo-dark) 0%, var(--photo-mid) 40%, var(--photo-light) 75%, #f4efe6 100%);
  }
  .brand-mark {
    position: absolute; left: 708px; top: 30px; width: 230px; height: 230px;
    border-radius: 50%; background: var(--black); color: var(--white);
    display: flex; flex-direction: column; align-items: center; justify-content: center;
    font-weight: 500; font-size: 44px; line-height: 1.05; letter-spacing: 1px; text-transform: uppercase;
  }
  .partners-strip {
    position: absolute; left: 520px; top: 309px; width: 680px; height: 102px;
    background: var(--strip);
  }
  .accreditation {
    position: absolute; left: 0; width: 680px; top: 10px; text-align: center;
    font-weight: 700; font-size: 18px; color: var(--ink);
  }
  .partner-list {
    position: absolute; left: 24px; right: 20px; top: 58px;
    display: flex; justify-content: space-between; align-items: center;
    font-weight: 700; font-size: 16px; color: var(--ink); text-transform: uppercase;
  }
  .partner-scheme { display: flex; align-items: center; gap: 6px; font-size: 14px; text-transform: none; }
  .partner-scheme::before {
    content: ""; width: 16px; height: 16px; background: var(--ink);
  }
</style>
</head>
<body>
<div class="banner">
  <section class="info-panel">
    <div class="staff-offer">10% OFF<br>for all<br>PCW Staff</div>
    <div class="services">
      Bike Hire<br>Repairs &amp; Servicing<br>Parts &amp; Accesories<br>New Bikes via Ridepathplan<br>Used Bikes for Sale
    </div>
    <div class="direction">
      <svg width="520" height="74" viewBox="0 0 520 74" aria-hidden="true">
        <polygon points="24,37 88,0 520,0 520,74 88,74" fill="var(--black)"/>
      </svg>
      <p class="direction-text">We're at the Halvercombe Institute<br>(next to Staff Hall, H12)</p>
    </div>
    <p class="phone">Call 0800 555 0147</p>
    <p class="web">www.pondelwheels.org.uk &nbsp;·&nbsp; info@pondelwheels.org.uk</p>
  </section>

  <div class="photo-area" role="img" aria-label="Photo of a cyclist in a checked shirt riding a bike through the city in warm sunlight"></div>

  <div class="brand-mark"><span>Pondel</span><span>Wheels</span></div>

  <section class="partners-strip">
    <p class="accreditation">All Mechanics Vestra Trained and Approved</p>
    <div class="partner-list">
      <span>Palmwick</span>
      <span>Vornastel</span>
      <span>Tavoli</span>
      <span>Oskel</span>
      <span>Vush</span>
      <span>Lappet</span>
      <span>Quill</span>
      <span class="partner-scheme">ridepathplan</span>
    </div>
  </section>
</div>
</body>
</html>
```